Lunar Ledger - Minimalistic Single Page Web Design

Project: We are in the process of creating a new Corp Identity. Design a website for our company incorporating the Logo recently designed and selected from a SketchHive contest. (attached)

Designers: For this project, you need to design a minimalistic single page, modern website. Beside text and image placement, you will also need to describe user interface, how content is presented and so on.
- Design Layout
- Design Image placements (if any)
- Design menu and buttons
- Design menu and buttons placements
- Design content layout
- Design overall effect and feel of website
- Design color scheme
- Design content style (tone and style of content, words type, how much)
- Design user interface (how do you scroll, what happens when you mouseover buttons, where do certain links and buttons lead you)

Coding Requirements: You need to design the website with a modern perspective on website visuals and effects. Jquery, HTML5 (no FLASH please). You do not need to code for this particular contest, but if you can also code, great, tell me and let me know how I can hire you to complete it. If you know someone that can code your vision, great, let me know. If not, you need to be clear and concise, and be willing to help me communicate with a developer to get the site executed. The web site needs to be modern and dynamic.

Company Name:
Lunar Ledger; Lunar-Ledger; LunarLedger

Domain: www.lunar-ledger.example

Company Industry:
Lunar Ledger provides consulting in areas of finance, accounting, business organization, and set up.
- Bookkeeping
- Project Management
- Budget Management
- Cash Management
- Receipt Management
- Filing and Records Management
- Training of administration and accounting staff
- Financial Reports
- Spreadsheets
- Graphs, charts and trend analysis
- Business set up
- Tax filings
- Payroll and HR

Clients:
- Small to medium size businesses
- Proprietors
- Entrepreneurs
- Mom & Pops Shops
- We cater to every industry

Corporate Identity:
- Past: I have never complete a webpage for my company. I did scratch several projects that were started and never completed. I fell in love with stick figures, whimsical designs, similar to that of "Cratebin", I believed in simplicity and minimalism. However, I was not effective in find the right people to complete my project. Bits and pieces of the website was designed, but never executed.

- Current: I need a webpage design. The web design must align with the current logo aesthetics.The current logo is new. I selected this logo for its simplicity and modern feel. It also incorporated an image of a trending graph, which fits with my company's profile. Still, I am leaning towards simple design, minimalism with boldness. I like my new webpage to be mature and professional, but I want it to portray energy and youth. So no "traditional corp" like design. I like new HTML5 elements, jquery and fun and beautiful forms and buttons. Less image is more.

Note: Please improvise according to your taste and professional perspective, you do not have to follow my suggestions word for word.

Features & Layout:
- Single page layout
- Vertical scroll
- Framed sections so that it looks good on the screen
- Well designed and strategically placed menu bar
- Fills a modern browser
- Beautiful color scheme that pops
- Incorporate Logo aesthetics

Fonts and Type:
- This is an element of the overall design
- I love clean fonts
- Fonts that adds meaning to the overall effect
- Clean

Sounds
- Please no cheesy sounds and background music

Images:
- To your liking
- But please, no lame corp people in suits
- No lame photographs
- I like stick figures
- I like whimsical illustrations

Landing Page:
- This should be the bulk of your design
- The landing page must be impressive, eye catchy
- Bold

Menu Bar:
- Header (introduction and landing page)
- Service & Products
- Company (about us)
- Affiliates and Clients (reference area)
- Contact (contact us area)
- Footer

Colors:
- Up to you, I just like things clean and easy to read
- No black background behind text
- Incorporate Logo Colors

Web Effects:
- According to your liking
- You will need to be involve to communicate the layout and design to the developer, so you need to be clear in your design.

Content:
- You personally don't have to come up with the content, but if you can great.
- I will help come up with the content throughout the contect timeframe, just let me know what you want
- I do not like too much content in my website. The most for each section is 2-3 lines if any.
- Combination could also be one liners.
- I like minimalistic approach.
- If you are not creating the final content, you need to show what type of content need to be created and in what style or tone.

Samples and Inspirations:
- http://scrollkin.example/
- http://zentrovo.example/#top
- http://brightmopservices.example/#about
- http://pixelgazette.example/inspiration/23-inspiring-single-page-designs
- http://www.tobiaskernstudio.example/
- http://www.ravelquist.example/

This I do not want:
- Too much popups (none if possible)
- Images of people
- Images of people in suits
- Stereotypical images of accountants
- Scrolling marquee
- Clip arts
Updates

Designers, I want to stress the fact that I am looking for a design, not simply a website. The website is 1 page long. Text and content should be minimal. So this means that the design has to do most of the talking. Please do not submit template like web designs, I can pull this off myself if needed. I need you to design a great header, footer and the connecting tissue from landing to end of the page. The entire design needs to flow.

Again, please do not use images of corp people or anything like that. Please think outside the box in how you want to express the company.

Some ideas:
An illustration from beginning to end of the website, have a story.
Add colors to the back ground. 
The background should not get in the way of reading the text, but it does not have to be boring.
Be bold in your design.

Also, please describe more about your design when you submit. Please don't submit a template like design and have no explanation for your actions.

Also, fee free to ask me questions. I am here to help. I check this everyday, so please contact if you need anything.

Designers, please read the details of my post before you submit the design.

If you have a great concept idea but is worry, you can go ahead and submit a pencil draft and ask my opinion before you work anymore on it.

Please see the website samples below for what I am really looking for:

Reason: Hi everyone, I am extending the deadline. It looks like some design are still pending completion, and I want you to have enough time to work on it.

Industry/Entity Type

Accounting

```html
<!DOCTYPE html>
<html lang="en">
<head>
<meta charset="utf-8">
<title>Lunar Ledger</title>
<link href="https://fonts.googleapis.com/css2?family=Arimo:wght@400;700&display=swap" rel="stylesheet">
<style>
:root{
  --navy:#0c2a7e;
  --deep:#0f2b45;
  --ocean:#1d5b82;
  --lime:#aabf2b;
  --lime-dark:#8fa412;
  --lime-text:#c3d92f;
  --teal:#6ccbd8;
  --grey:#ededed;
  --band:#3a3a3a;
  --white:#ffffff;
  --ink:#333333;
  --field:#8a8a8a;
}
*{box-sizing:border-box;margin:0;padding:0}
html,body{width:932px;height:1200px;overflow:hidden}
body{position:relative;font-family:"Arimo",Arial,sans-serif;background:var(--grey);color:var(--ink)}
.abs{position:absolute}

/* top stage */
.stage{left:0;top:0;width:932px;height:610px;
  background:linear-gradient(160deg,#27678f 0%,#1b5478 35%,#143d5c 70%,#0f2a40 100%)}
.stage-shade{left:0;top:0;width:932px;height:610px;
  background:linear-gradient(120deg,rgba(255,255,255,0.05) 0 40%,rgba(0,0,0,0) 40% 100%)}

/* header */
.header{left:70px;top:35px;width:792px;height:78px;background:var(--white);border-radius:3px;box-shadow:0 1px 4px rgba(0,0,0,.3)}
.brand{left:16px;top:15px;font-size:36px;color:var(--navy);letter-spacing:.5px;display:flex;align-items:center;gap:8px}
.brand-dot{width:12px;height:12px;border-radius:50%;background:var(--lime)}
.nav{right:10px;top:22px;display:flex;gap:0;font-size:12px}
.nav a{color:#222;text-decoration:none;padding:5px 10px;margin-left:10px;height:22px;line-height:12px}
.nav a.active{background:var(--lime);color:var(--white);border-radius:2px}

/* hero */
.hero{left:70px;top:124px;width:792px;height:257px;border-radius:3px;overflow:hidden;
  background:linear-gradient(90deg,#5ec0cf 0%,#72cfdb 50%,#66c5d3 100%)}
.hero-art{left:400px;top:0;width:392px;height:257px;
  background:linear-gradient(150deg,rgba(255,255,255,.18),rgba(255,255,255,.05) 60%,rgba(240,240,250,.6) 100%)}
.hero-title{left:40px;top:56px;font-size:20px;color:var(--white)}
.hero-text{left:41px;top:88px;width:320px;font-size:10.3px;line-height:17.8px;color:var(--white)}
.btn-more{left:42px;top:151px;width:81px;height:23px;background:linear-gradient(#555,#2e2e2e);
  color:var(--white);font-size:10px;line-height:23px;text-align:center;border-radius:2px;border:1px solid #222}
.dots{left:19px;top:228px;display:flex;gap:11px}
.dots span{width:10px;height:10px;border-radius:50%;background:#4b9aa6}
.dots span.on{background:var(--lime);box-shadow:0 0 0 2px var(--white)}

/* welcome */
.welcome-title{left:82px;top:410px;font-size:19.5px;color:var(--lime-text)}
.welcome-text{left:82px;top:452px;width:772px;font-size:10.3px;line-height:17.8px;color:var(--white)}
.welcome-text p+p{margin-top:6px}

/* bands and tabs */
.band{left:0;width:932px;height:5px;background:var(--band)}
.tab{left:272px;width:388px;background:var(--white);border:1px solid #d8d8d8;border-radius:2px;
  text-align:center;color:#333;box-shadow:0 1px 3px rgba(0,0,0,.15)}

/* services */
.card{top:658px;width:156px;height:188px;background:var(--white);border:1px solid #8cc4e8;padding:4px}
.card-img{width:146px;height:134px}
.card-num{left:50%;top:-2px;transform:translateX(-50%);width:46px;height:24px;border-radius:0 0 23px 23px;
  background:var(--white);color:#2d6fb0;font-size:13px;text-align:center;line-height:20px}
.card-label{width:146px;height:45px;background:var(--navy);color:var(--white);font-weight:700;font-size:13.5px;
  display:flex;align-items:center;justify-content:center;text-align:center;line-height:14px}

/* contact */
.contact{left:0;top:899px;width:932px;height:240px;background:var(--lime)}
.field{background:var(--white);border:1px solid #d9d9d9;border-bottom:4px solid #e6e6e6;border-radius:2px;
  font-size:11px;color:var(--field);padding:9px 11px}
.submit{left:783px;top:1092px;width:80px;height:31px;background:linear-gradient(#5a5a5a,#333);color:#ddd;
  font-size:13px;font-weight:700;text-align:center;line-height:31px;border-radius:2px;border:1px solid #222}

/* footer */
.footer{left:0;top:1139px;width:932px;height:61px;background:var(--lime-dark);color:var(--white);font-size:10px}
.foot-links{left:69px;top:12px}
.foot-links span{margin:0 5px}
.copy{left:69px;top:36px}
.social{top:18px;width:23px;height:23px;border-radius:50%;background:var(--white);border:1px solid #d0d0d0}
</style>
</head>
<body>

<div class="abs stage"></div>
<div class="abs stage-shade"></div>

<header class="abs header">
  <div class="abs brand">lunarledger<span class="brand-dot"></span></div>
  <nav class="abs nav">
    <a class="active" href="#home">HOME</a>
    <a href="#about">ABOUT</a>
    <a href="#services">SERVICES</a>
    <a href="#contact">CONTACT</a>
  </nav>
</header>

<section class="abs hero" id="home">
  <div class="abs hero-art" role="img" aria-label="Hand drawing a rising bar chart with an upward arrow in white chalk"></div>
  <h1 class="abs hero-title" style="font-weight:400">Finance Consulting</h1>
  <p class="abs hero-text">Donec scelerisque gravida feugiat. Maecenas non magna ipsum, nec faucibus turpis. Vestibulum vestibulum arcu vitae tellus con nisl tincidunt nec nisi ac neque aliquam laoreet.</p>
  <div class="abs btn-more">VIEW MORE</div>
  <div class="abs dots"><span class="on"></span><span></span><span></span><span></span></div>
</section>

<h2 class="abs welcome-title" id="about" style="font-weight:400">Welcome to our site</h2>
<div class="abs welcome-text">
  <p>Donec scelerisque gravida feugiat. Maecenas non magna ipsum, nec faucibus turpis. Vestibulum vestibulum arcu vitae tellus consectetur tincidunt. Nulla placerat luctus massa, sit amet dignissim nisl tincidunt a. Maecenas nec nisi ac neque aliquam laoreet. Sed quis egestas dui. Nullam nisi tellus, facilisis a mattis in, sodales ut odio. Donec quis nibh purus, in ullamcorper metus. Etiam rhoncus elit elit. Phasellus elementum, justo ac scelerisque interdum, metus odio pulvinar velit, ut commodo tellus arcu nec nisl. Aliquam interdum, urna faucibus dignissim imperdiet, tortor sem iaculis nulla, vel adipiscing elit turpis feugiat neque.</p>
  <p>Nulla non convallis lectus. Phasellus sed ante sit amet sapien elementum fermentum vel sit amet diam. Ut facilisis, justo id imperdiet consequat, ante eros ornare odio, nec convallis nunc tellus eu felis.</p>
</div>

<div class="abs band" style="top:610px"></div>
<div class="abs tab" id="services" style="top:594px;height:36px;font-size:16.5px;line-height:34px">Lunar Ledger provides consulting in areas of...</div>

<div class="abs card" style="left:82px">
  <div class="card-img" role="img" aria-label="Seedling growing from coins in an open hand" style="background:linear-gradient(180deg,#f7f7f7 0%,#efe6dc 55%,#d8b58f 80%,#f4f4f4 100%)"></div>
  <div class="abs card-num">1</div>
  <div class="card-label">Finance</div>
</div>
<div class="abs card" style="left:287px">
  <div class="card-img" role="img" aria-label="Stack of coins on a printed stock chart" style="background:linear-gradient(160deg,#3d5470 0%,#8ea3ba 45%,#c9d4e0 100%)"></div>
  <div class="abs card-num">2</div>
  <div class="card-label">Accounting</div>
</div>
<div class="abs card" style="left:492px">
  <div class="card-img" role="img" aria-label="Team silhouettes in front of a world map" style="background:linear-gradient(180deg,#b9c6d6 0%,#e8edf3 50%,#5a6370 100%)"></div>
  <div class="abs card-num">3</div>
  <div class="card-label">Business<br>Organization</div>
</div>
<div class="abs card" style="left:697px">
  <div class="card-img" role="img" aria-label="Silhouettes meeting in a bright office" style="background:linear-gradient(180deg,#e2e6ec 0%,#a8b2bf 50%,#3b4350 100%)"></div>
  <div class="abs card-num">4</div>
  <div class="card-label">Business<br>Set up</div>
</div>

<section class="abs contact" id="contact">
  <div class="abs field" style="left:69px;top:46px;width:258px;height:32px">First name</div>
  <div class="abs field" style="left:337px;top:46px;width:259px;height:32px">Last name</div>
  <div class="abs field" style="left:605px;top:46px;width:258px;height:32px">Company name</div>
  <div class="abs field" style="left:69px;top:87px;width:258px;height:32px">Phone</div>
  <div class="abs field" style="left:337px;top:87px;width:259px;height:32px">Email</div>
  <div class="abs field" style="left:605px;top:87px;width:258px;height:32px">Fax</div>
  <div class="abs field" style="left:69px;top:128px;width:794px;height:56px">Comment</div>
</section>
<div class="abs submit">SUBMIT</div>

<div class="abs band" style="top:894px"></div>
<div class="abs tab" style="top:877px;height:37px;font-size:16.5px;line-height:35px">Contact us</div>

<footer class="abs footer">
  <div class="abs foot-links">Home<span>|</span>About<span>|</span>Services<span>|</span>Contact</div>
  <div class="abs copy">Copyright &nbsp;©&nbsp; 2013 &nbsp; www.lunar-ledger.example &nbsp;&nbsp; All rights reserved.</div>
  <div class="abs social" style="left:810px" aria-label="Social profile"></div>
  <div class="abs social" style="left:839px" aria-label="Social profile"></div>
</footer>

</body>
</html>
```